VelaMarina Passport 4 Page A5 Brochure

DESIGN BRIEF – VelaMarina Passport Brochure
Project Title
VelaMarina Passport – A5 4-Page Brochure Design
________________________________________
Overview
We are looking for a designer to create a clean, visually appealing A5, 4-page brochure to present The VelaMarina Passport to local businesses.
The brochure will be used as a sales and information document and should feel:
• Premium
• Friendly
• Professional
• Easy to understand
• Fun and engaging
The audience is bar owners, venue managers, restaurants, clubs, hotels, and local businesses in Maspalomas.
Format & Technical Requirements
• Size: A5
• Pages: 4 (front cover, 2 inside pages, back cover)
• Orientation: Portrait
• Print-ready design
• Space-aware layouts (some content will be added later)
Brand & Tone
• Brand: VelaMarina
• Location: Maspalomas / Gran Canaria
• Target audience: LGBTQ+ friendly venues and tourism businesses
• Style:
o Modern
o Warm
o Professional
o Island-inspired
o Not overly corporate
• Avoid clutter — white space is welcome
PAGE-BY-PAGE REQUIREMENTS
PAGE 1 – FRONT COVER
Purpose: First impression & visual impact
Requirements:
• Strong visual design
• Clear title: “The VelaMarina Passport”
• Subheading example:
A premium voucher booklet connecting tourists with local venues
• Leave a clear placeholder space for:
o An image of the Passport front cover
• We are open to designers also proposing a design for the Passport front cover itself (optional extra – happy to receive bids for this)
Style notes:
• Eye-catching but elegant
• Feel of travel, discovery, nightlife, and local culture
PAGE 2 – INSIDE LEFT
Purpose: Explain the concept – text provided
Content:
• Short overview of:
o What The VelaMarina Passport is
o Targeted distribution
o Key benefits (high-value visitors, no wasted reach, transferable, no expiry)
• Icons or visual blocks encouraged
• Easy-to-scan layout
Design Notes:
• Use headings, icons, or info blocks
• Avoid large walls of text
PAGE 3 – INSIDE RIGHT (How the Passport Works in Practice)
Purpose:
To visually explain how The VelaMarina Passport is owned, transferred, and used, while showing real examples of how venues appear inside the booklet.
Required Elements
1. Passport Ownership & Transfer Section
The Passport can be owned by up to three people in total (original owner + two transfers).
This page should include three clearly defined visual placeholders representing:
• Original Passport Owner
• Transfer 1 – New Owner
• Transfer 2 – Final Owner
These can be shown as:
• Three mini page mockups
• Three outlined boxes with headings
• Or a creative, passport-style visual layout
Each section should clearly show space for:
• Name
• Country (optional)
• Signature
• Date
👉 We are open to creative proposals for the design of this transfer page and happy to receive bids specifically for designing this page as part of the Passport.
2. Example Voucher Advert Section
This page should also include space to show an example of a voucher advert page, displayed as a mock layout only.
The example should visually communicate:
• Venue name & logo
• Short venue description
• Example offer (e.g. “Free signature shot”)
• Voucher box to be crossed off by staff
This is illustrative only — final content will be provided later.
Design Notes
• Keep the layout clear and easy to understand at a glance
• Visual explanation is more important than text
• Use icons, borders, or soft background panels to separate sections
• The tone should feel official but friendly, similar to a real passport
• Avoid clutter — white space is encouraged
Key Message to Communicate Visually
• The Passport has real ownership
• It can be passed on
• Vouchers are clearly controlled
• Each page feels premium, structured, and easy to use
PAGE 4 – BACK COVER
Purpose: Commercial offer & call to action
Content requirements:
• Clear presentation of two participation options:
1. Voucher Page (incentivised pricing)
2. Standard Advertising Page (no voucher)
• Simple comparison layout encouraged
Visual placeholders required:
• Space to show:
o A sample voucher page
o A sample advert-only page
Contact Details Area:
• VelaMarina logo or name
• Contact text placeholder (phone / email / website)
• Clean, professional call to action
Design Flexibility
We are happy to:
• Receive creative layout suggestions
• See optional icon sets
• See colour palette ideas
• Receive proposals that slightly refine the structure (as long as all elements are included)
Deliverables
• Final A5 4-page brochure design
• Print-ready PDF
• Editable source files (preferred)
• Clear indication of any optional extras (e.g. Passport cover design)
What We’re Looking For
• Clean layout
• Strong hierarchy
• Clear visual storytelling
• Understanding of hospitality / nightlife / tourism
• Ability to balance fun with professionalism
Optional Extras (welcome but not required)
• Proposal for the Passport front cover design
• Proposal for the transfer page design
• Icon set or mini graphic elements
• Alternative colour version
Notes to Designers
This brochure will be used repeatedly and updated over time, so clarity, flexibility, and strong structure are more important than heavy decoration.
We look forward to creative, thoughtful proposals.

Target Market(s)

LGBTIQ+ Tourists and Businesses

Industry/Entity Type

Tourism

Requirements
Must have
• meet the 4 page brief
Nice to have
• proposals for design elements within the design

```html
<!DOCTYPE html>
<html lang="en">
<head>
<meta charset="utf-8">
<title>VelaMarina Passport – A5 Brochure</title>
<link href="https://fonts.googleapis.com/css2?family=Montserrat:wght@400;500;600;700;800&family=Pacifico&display=swap" rel="stylesheet">
<style>
:root{
  --stage:#e4ebf3;
  --navy:#1b2f78;
  --blue:#1f5cc4;
  --sky:#3f8fe0;
  --orange:#f29a1f;
  --yellow:#f7d44c;
  --cream:#fbf7ec;
  --ink:#2e3440;
  --muted:#7a8190;
  --ticket:#2a1d5e;
  --white:#ffffff;
}
*{box-sizing:border-box;margin:0;padding:0}
html,body{width:851px;height:1200px;overflow:hidden}
body{background:var(--stage);font-family:'Montserrat',sans-serif;color:var(--ink);position:relative}
.spread{position:absolute;left:51px;width:750px;height:552px;display:flex;box-shadow:0 4px 14px rgba(20,40,80,.18)}
.spread--outer{top:28px}
.spread--inner{top:618px;background:var(--white)}
.page{position:relative;width:375px;height:100%;overflow:hidden}

/* back cover */
.back-cover{background:linear-gradient(180deg,#1d4fae 0%,#1a3f96 45%,#173486 100%);color:var(--white)}
.back-cover__photo{position:absolute;left:0;top:0;width:100%;height:230px;background:linear-gradient(180deg,#2d6fc8 0%,#1b4aa6 70%,rgba(26,63,150,0) 100%)}
.brand{display:flex;align-items:center;gap:8px;justify-content:center}
.brand__dot{width:26px;height:26px;border-radius:50%;background:var(--yellow);flex:none}
.brand__name{font-weight:800;font-size:22px;letter-spacing:.5px}
.back-cover .brand{position:absolute;top:282px;left:0;right:0}
.back-cover .brand__name{color:var(--white)}
.back-cover__tag{position:absolute;top:316px;left:0;right:0;text-align:center;font-size:7px;letter-spacing:1px;opacity:.8}
.contact{position:absolute;left:0;right:0;text-align:center;font-size:13px;font-weight:500}
.contact svg{display:block;margin:0 auto 6px}
.contact--phone{top:392px}
.contact--web{top:440px}
.contact--social{top:490px}

/* front cover */
.front-cover{background:radial-gradient(ellipse at 70% 55%,#f9d96a 0%,#f7e39a 35%,var(--cream) 70%)}
.front-cover .brand{position:absolute;top:56px;left:0;right:0}
.front-cover .brand__name{color:var(--navy);font-size:20px}
.front-cover__tag{position:absolute;top:86px;left:0;right:0;text-align:center;font-size:6.5px;color:var(--muted);letter-spacing:1px}
.front-cover__photo{position:absolute;left:70px;top:110px;width:285px;height:300px;border-radius:50% 50% 8px 8px;background:radial-gradient(circle at 55% 45%,#f5b53a 0%,#f0c75c 50%,rgba(247,212,76,.3) 100%)}
.title{position:absolute;left:48px;top:416px;width:300px;line-height:1}
.title__the{font-family:'Pacifico',cursive;color:var(--orange);font-size:30px;display:inline-block;margin-right:4px}
.title__brand{font-weight:800;color:var(--navy);font-size:30px}
.title__word{display:block;font-weight:700;color:var(--orange);font-size:26px;margin:4px 0 0 70px}
.front-cover__sub{position:absolute;left:104px;top:498px;width:250px;font-size:11.5px;color:var(--navy);font-weight:500;line-height:1.3}

/* inside left */
.kicker{position:absolute;left:62px;top:22px;display:flex;align-items:center;gap:8px;color:var(--orange);font-size:13px;font-weight:700;letter-spacing:3px}
.kicker::before{content:"";width:34px;height:2px;background:var(--orange)}
.h2{font-weight:700;font-size:19px;color:var(--navy);line-height:1.15}
.h2 em{font-style:normal;color:var(--blue)}
.purpose__title{position:absolute;left:30px;top:44px;width:215px}
.body{font-size:9px;line-height:1.45;color:var(--ink)}
.purpose__text{position:absolute;left:30px;top:94px;width:210px}
.hiker{position:absolute;left:248px;top:8px;width:120px;height:146px;background:linear-gradient(180deg,#e9d3b4 0%,#c98f56 55%,#8a6a4e 100%);clip-path:polygon(35% 0,70% 0,100% 100%,0 100%)}
.distribution__title{position:absolute;left:120px;top:166px;font-size:17px;font-weight:700;color:var(--navy)}
.tent{position:absolute;left:12px;top:188px;width:96px;height:110px;background:linear-gradient(160deg,#f6c34a 0%,#f29a1f 60%,#5aa357 100%);border-radius:8px}
.distribution__cols{position:absolute;left:120px;top:196px;width:240px;display:flex;gap:14px}
.distribution__cols p{flex:1}
.benefits__title{position:absolute;left:24px;top:328px;font-size:19px;font-weight:700;color:var(--orange)}
.benefits__text{position:absolute;left:24px;top:362px;width:110px}
.benefits__panel{position:absolute;left:150px;top:310px;width:240px;height:260px;background:var(--blue);border-radius:60% 0 0 0 / 40% 0 0 0}
.benefits__panel .body{position:absolute;left:50px;top:60px;width:160px;color:var(--white)}
.benefits__panel .body + .body{top:128px;font-weight:600}

/* inside right */
.ownership__title{position:absolute;left:28px;top:24px;width:240px;font-size:20px}
.owners{position:absolute;left:28px;top:96px;width:322px;display:grid;grid-template-columns:repeat(3,1fr);gap:10px}
.owner__head{font-size:8px;color:var(--muted);margin-bottom:2px}
.owner__role{font-size:9.5px;font-weight:700;color:var(--blue);line-height:1.2;margin-bottom:8px}
.owner__field{font-size:8px;color:var(--ink);padding:6px 0 10px;border-bottom:1px solid #cfd6e2}
.owner__field small{font-size:6px;color:var(--muted)}
.voucher-zone{position:absolute;left:0;bottom:0;width:100%;height:190px;background:linear-gradient(180deg,rgba(247,212,76,0) 0%,#f9e17a 35%,var(--yellow) 100%)}
.voucher__title{position:absolute;left:28px;top:356px;width:180px;font-size:18px}
.voucher__text{position:absolute;left:216px;top:358px;width:140px}
.ticket{position:absolute;left:72px;top:420px;width:286px;height:108px;background:var(--ticket);border-radius:8px;color:var(--white);overflow:hidden}
.ticket::before,.ticket::after{content:"";position:absolute;left:-10px;top:44px;width:20px;height:20px;border-radius:50%;background:var(--yellow)}
.ticket::after{left:auto;right:-10px}
.ticket__label{position:absolute;left:28px;top:20px;font-size:9px;opacity:.85}
.ticket__name{position:absolute;left:28px;top:32px;font-size:15px;font-weight:700}
.ticket__text{position:absolute;left:28px;top:56px;width:140px;font-size:8px;line-height:1.4;opacity:.85}
.ticket__offer{position:absolute;left:178px;top:14px;background:var(--yellow);color:var(--ticket);font-size:9px;font-weight:700;padding:3px 8px;border-radius:3px}
.ticket__box{position:absolute;left:236px;top:30px;width:34px;height:50px;border:1.5px dashed rgba(255,255,255,.7);border-radius:3px}
</style>
</head>
<body>

<section class="spread spread--outer">
  <article class="page back-cover">
    <div class="back-cover__photo" role="img" aria-label="Underwater photo of divers in deep blue sea"></div>
    <div class="brand"><span class="brand__dot"></span><span class="brand__name">VelaMarina</span></div>
    <p class="back-cover__tag">THE PASSPORT TO LOCAL VENUES</p>
    <div class="contact contact--phone">
      <svg width="16" height="16" viewBox="0 0 24 24" fill="#f7d44c"><path d="M6.6 10.8a15.1 15.1 0 0 0 6.6 6.6l2.2-2.2a1 1 0 0 1 1-.25 11.4 11.4 0 0 0 3.6.57 1 1 0 0 1 1 1V20a1 1 0 0 1-1 1A17 17 0 0 1 3 4a1 1 0 0 1 1-1h3.5a1 1 0 0 1 1 1c0 1.250.2 2.450.57 3.570a1 1 0 0 1-.25 1z"/></svg>
      012 555 0148
    </div>
    <div class="contact contact--web">
      <svg width="16" height="16" viewBox="0 0 24 24" fill="none" stroke="#f7d44c" stroke-width="2"><circle cx="12" cy="12" r="9"/><path d="M3 12h18M12 3c3 3.5 3 14.5 0 18M12 3c-3 3.5-3 14.5 0 18"/></svg>
      www.velamarina.com
    </div>
    <div class="contact contact--social">
      <svg width="16" height="16" viewBox="0 0 24 24" fill="none" stroke="#f7d44c" stroke-width="2"><circle cx="12" cy="12" r="9"/><circle cx="12" cy="12" r="3"/></svg>
      velamarina.com/social
    </div>
  </article>

  <article class="page front-cover">
    <div class="brand"><span class="brand__dot"></span><span class="brand__name">VelaMarina</span></div>
    <p class="front-cover__tag">THE PASSPORT TO LOCAL VENUES</p>
    <div class="front-cover__photo" role="img" aria-label="Photo of a smiling traveller sitting on a red suitcase"></div>
    <h1 class="title"><span class="title__the">The</span><span class="title__brand">VelaMarina</span><span class="title__word">Passport</span></h1>
    <p class="front-cover__sub">A premium voucher booklet connecting tourists with local venues</p>
  </article>
</section>

<section class="spread spread--inner">
  <article class="page inside-left">
    <p class="kicker">PURPOSE</p>
    <h2 class="h2 purpose__title">What the <em>VelaMarina</em> Passport is?</h2>
    <p class="body purpose__text">Lorem ipsum dolor sit amet, consectetur adipiscing elit, sed do eiusmod tempor incididunt ut labore et dolore magna aliqua. Quis ipsum suspendisse ultrices gravida.</p>
    <div class="hiker" role="img" aria-label="Photo of a hiker standing on a rocky summit"></div>
    <h3 class="distribution__title">Targeted Distribution</h3>
    <div class="tent" role="img" aria-label="Illustration of a camping tent among trees"></div>
    <div class="distribution__cols">
      <p class="body">Lorem ipsum dolor sit amet, consectetur adipiscing elit, sed do eiusmod tempor.</p>
      <p class="body">Quis ipsum suspendisse ultrices gravida. Risus commodo viverra.</p>
    </div>
    <h3 class="benefits__title">Key Benefits</h3>
    <p class="body benefits__text">Lorem ipsum dolor sit amet, consectetur adipiscing elit. Quis ipsum suspendisse ultrices gravida.</p>
    <div class="benefits__panel">
      <p class="body">Lorem ipsum dolor sit amet, consectetur adipiscing elit, sed do eiusmod tempor. Quis ipsum suspendisse ultrices.</p>
      <p class="body">Lorem ipsum dolor sit amet, consectetur adipiscing elit.</p>
    </div>
  </article>

  <article class="page inside-right">
    <h2 class="h2 ownership__title"><em>Passport</em> Ownership And Transfer</h2>
    <div class="owners">
      <div class="owner">
        <p class="owner__head">Original</p>
        <p class="owner__role">Passport Owner</p>
        <p class="owner__field">Name</p>
        <p class="owner__field">Country <small>(optional)</small></p>
        <p class="owner__field">Signature</p>
        <p class="owner__field">Date</p>
      </div>
      <div class="owner">
        <p class="owner__head">Transfer 1</p>
        <p class="owner__role">New Owner</p>
        <p class="owner__field">Name</p>
        <p class="owner__field">Country <small>(optional)</small></p>
        <p class="owner__field">Signature</p>
        <p class="owner__field">Date</p>
      </div>
      <div class="owner">
        <p class="owner__head">Transfer 2</p>
        <p class="owner__role">Final Owner</p>
        <p class="owner__field">Name</p>
        <p class="owner__field">Country <small>(optional)</small></p>
        <p class="owner__field">Signature</p>
        <p class="owner__field">Date</p>
      </div>
    </div>
    <div class="voucher-zone"></div>
    <h2 class="h2 voucher__title"><em>VelaMarina</em> Passport Voucher</h2>
    <p class="body voucher__text">Lorem ipsum dolor sit amet, consectetur adipiscing elit, sed do eiusmod tempor.</p>
    <div class="ticket">
      <p class="ticket__label">Lorem Ipsum</p>
      <p class="ticket__name">Lorem Ipsum</p>
      <p class="ticket__text">Quis ipsum suspendisse ultrices gravida. Risus commodo viverra.</p>
      <span class="ticket__offer">10% Off</span>
      <span class="ticket__box"></span>
    </div>
  </article>
</section>

</body>
</html>
```